Business card design needed for Automotive Reconditioning business

I have a logo design i just cant decide on the best color or layout for the business card, I will upload all the files so you can see all colors schemes we are considering. I have other file formats if needed let me know.

Target Market(s)

automotive dealerships

Contact Information for Business Card

HERE are the Descriptions and info needed on the card:
Interior Repair: Leather carpet burns panels dash Deoderize
Dealer products and Vin Verify
( spot for name and cell number) My name is Norman Bexley phone 614 352-4180 Title COO www.QuorvalMotive.com

Font styles to use
Sans Serif
Other font styles liked:
• what ever you think looks best

Requirements
Must have
• Must be able to change the name and phone for employees

```html
<!DOCTYPE html>
<html lang="en">
<head>
<meta charset="utf-8">
<title>Quorval Motive – Business Card</title>
<link href="https://fonts.googleapis.com/css2?family=Ubuntu:wght@400;500;700&display=swap" rel="stylesheet">
<style>
  :root {
    --page-bg: #e9e6e1;
    --card-white: #ffffff;
    --brand-red: #e2452a;
    --brand-red-deep: #c42f1b;
    --brand-blue: #2aa3da;
    --brand-blue-deep: #1b4c9e;
    --text-grey: #9c9c9c;
    --text-white: #ffffff;
  }
  * { margin: 0; padding: 0; box-sizing: border-box; }
  html, body {
    width: 1200px;
    height: 780px;
    overflow: hidden;
    background: var(--page-bg);
    font-family: "Ubuntu", Arial, sans-serif;
  }
  .canvas {
    width: 1200px;
    height: 780px;
    display: flex;
    align-items: center;
    justify-content: center;
  }
  .business-card {
    position: relative;
    width: 1050px;
    height: 600px;
    background: var(--card-white);
    box-shadow: 0 10px 30px rgba(0,0,0,0.18);
    overflow: hidden;
  }
  .card-bands {
    position: absolute;
    inset: 0;
    width: 100%;
    height: 100%;
  }
  .brand-lockup {
    position: absolute;
    left: 390px;
    top: 162px;
    display: flex;
    align-items: center;
    gap: 16px;
    white-space: nowrap;
  }
  .brand-dot {
    width: 28px;
    height: 28px;
    border-radius: 50%;
    background: var(--brand-blue);
    flex: none;
  }
  .brand-name {
    font-weight: 700;
    font-size: 46px;
    letter-spacing: 1px;
    text-transform: uppercase;
    color: var(--brand-red);
  }
  .contact-block {
    position: absolute;
    left: 305px;
    top: 300px;
    color: var(--text-grey);
    white-space: nowrap;
  }
  .person-name {
    font-size: 34px;
    font-weight: 500;
    color: var(--brand-red);
    line-height: 1.15;
  }
  .person-title {
    font-size: 22px;
    line-height: 1.3;
    margin-bottom: 16px;
  }
  .address-line {
    font-size: 21px;
    line-height: 1.35;
  }
  .address { margin-bottom: 14px; }
  .contact-line {
    display: flex;
    align-items: center;
    gap: 10px;
    font-size: 21px;
    line-height: 1.5;
  }
  .contact-icon {
    width: 24px;
    height: 24px;
    flex: none;
  }
  .service-list {
    position: absolute;
    right: 60px;
    bottom: 92px;
    text-align: right;
    font-size: 16px;
    line-height: 1.45;
    color: var(--text-white);
    white-space: nowrap;
  }
  .website {
    position: absolute;
    right: 60px;
    bottom: 42px;
    font-size: 26px;
    font-weight: 500;
    color: var(--text-white);
    letter-spacing: 0.5px;
  }
</style>
</head>
<body>
<main class="canvas">
  <section class="business-card">
    <svg class="card-bands" viewBox="0 0 1050 600" aria-hidden="true">
      <defs>
        <linearGradient id="red-band" x1="0" y1="1" x2="1" y2="0">
          <stop offset="0" stop-color="var(--brand-red-deep)"/>
          <stop offset="1" stop-color="var(--brand-red)"/>
        </linearGradient>
        <linearGradient id="blue-band" x1="1" y1="0" x2="0" y2="1">
          <stop offset="0" stop-color="var(--brand-blue)"/>
          <stop offset="1" stop-color="var(--brand-blue-deep)"/>
        </linearGradient>
      </defs>
      <path d="M0 0 H1050 V14 C600 20 200 140 170 600 H0 Z" fill="url(#red-band)"/>
      <path d="M1050 14 V600 H0 V590 C700 588 940 420 920 14 Z" fill="url(#blue-band)"/>
    </svg>

    <div class="brand-lockup">
      <span class="brand-dot"></span>
      <span class="brand-name">Quorval Motive</span>
    </div>

    <div class="contact-block">
      <p class="person-name">Norman Bexley</p>
      <p class="person-title">COO</p>
      <div class="address">
        <p class="address-line">PO Box 418, Harlow Road</p>
        <p class="address-line">Columbus OH</p>
      </div>
      <p class="contact-line">
        <svg class="contact-icon" viewBox="0 0 26 26" aria-hidden="true">
          <rect width="26" height="26" rx="5" fill="var(--brand-red)"/>
          <path d="M8 6 L11 6 L12 10 L10 11.5 C11 14 12 15 14.5 16 L16 14 L20 15 L20 18 C20 19 19 20 18 20 C11 19.5 6.5 15 6 8 C6 7 7 6 8 6 Z" fill="#fff"/>
        </svg>
        614 352-4180
      </p>
      <p class="contact-line">
        <svg class="contact-icon" viewBox="0 0 26 26" aria-hidden="true">
          <rect width="26" height="26" rx="5" fill="var(--brand-red)"/>
          <rect x="5.5" y="8" width="15" height="10.5" rx="1" fill="none" stroke="#fff" stroke-width="1.8"/>
          <path d="M6 8.5 L13 14 L20 8.5" fill="none" stroke="#fff" stroke-width="1.8"/>
        </svg>
        info@quorvalmotive.com
      </p>
    </div>

    <div class="service-list">
      <p>Interior Repair · Deodorize</p>
      <p>Dealer Products · VIN Verify</p>
    </div>

    <p class="website">www.QuorvalMotive.com</p>
  </section>
</main>
</body>
</html>
```